Quillfield Gallery Ridge Campus

Design cover and inside pages. - will fill in the rest later. I just have some ideas here. This is a marketing brochure for a new building - raising money. Should look professional - but this is an art gallery, so can have color. I wouldn't also mind seeing some chrome effects. I put some samples of fun ideas, but I am open. This is to get people exciting to give to the campaign to raise money for the new building
Target Market(s)
People who would like to donate to a new art gallery - the local community
Requirements
Must have
- The end product, after it is cut down from full bleed, should be 8.25 X 8.25.
Nice to have
- Should be modern and and exciting. The one thing is to show the problem and how we are going to solve it.. Something like "challenge" and resolution"..
- Would like it to go along with this idea of evolve - something new and improved and exciting.. with a very modern look. YOu will see that the logo is three different gradients of orange.. these can change to another color - it doesn't have to be orange.. I would like to see less orange used. The font on the old building is art deco.. so I see that the font for this should be non-serif
Should not have
- I have had designers use the logo as an overlay over pictures - I would like to get away from that.

```html
<!DOCTYPE html>
<html lang="en">
<head>
<meta charset="utf-8">
<title>Quillfield Gallery Ridge Campus – Brochure</title>
<link href="https://fonts.googleapis.com/css2?family=Open+Sans:wght@400;600;700&family=Libre+Baskerville:wght@400;700&display=swap" rel="stylesheet">
<style>
  :root{
    --backdrop:#8c8c8c;
    --white:#ffffff;
    --ink:#1d1d1d;
    --body-ink:#2b2b2b;
    --orange:#f6a23a;
    --pink:#ec2f8c;
    --magenta:#c41f95;
    --violet:#8e2a9e;
    --frame:#f27bb8;
    --sketch:#e9e9e9;
    --sketch-line:#bdbdbd;
    --sans:"Open Sans", Arial, sans-serif;
    --serif:"Libre Baskerville", Georgia, serif;
  }
  *{margin:0;padding:0;box-sizing:border-box}
  html,body{width:1200px;height:2400px;overflow:hidden}
  body{background:var(--backdrop);position:relative;font-family:var(--sans);color:var(--ink)}

  .spread{position:absolute;left:53px;width:1099px}
  .abs{position:absolute}

  /* cover spread */
  .cover{top:48px;height:1140px;overflow:hidden;
    background:
      radial-gradient(ellipse 520px 420px at 120px 80px, var(--orange) 0%, rgba(246,162,58,0) 100%),
      radial-gradient(ellipse 500px 300px at 820px 40px, rgba(255,255,255,.95) 0%, rgba(255,255,255,0) 100%),
      radial-gradient(ellipse 420px 360px at 560px 120px, rgba(246,162,58,.85) 0%, rgba(246,162,58,0) 100%),
      radial-gradient(ellipse 600px 420px at 300px 1100px, var(--violet) 0%, rgba(142,42,158,0) 100%),
      linear-gradient(180deg, #f27a5c 0%, var(--pink) 45%, var(--magenta) 80%, #a82a9c 100%);
  }
  .panel-fold{left:547px;top:0;width:1px;height:100%;background:rgba(255,255,255,.15)}

  .contact{left:0;width:547px;top:190px;text-align:center;color:var(--white);font-size:22px;line-height:45px}

  .thumb{width:168px;height:161px;border:6px solid var(--frame);box-shadow:0 0 0 2px rgba(255,255,255,.35)}
  .thumb-1{left:72px;top:403px;background:linear-gradient(135deg,#f2c94c,#e84f3c 50%,#3a6fd0)}
  .thumb-2{left:269px;top:403px;background:linear-gradient(160deg,#d8cfb0,#b6553a 60%,#7a3a2a)}
  .thumb-3{left:72px;top:595px;background:linear-gradient(135deg,#f4b63e,#e07a2a 50%,#f3e2b0)}
  .thumb-4{left:269px;top:595px;background:linear-gradient(135deg,#3b3550,#6c5a8a 50%,#c9a84a)}

  .brand{display:flex;align-items:center;gap:14px;color:var(--white);font-family:var(--sans);font-weight:600}
  .brand-mark{width:70px;height:70px;border-radius:50%;background:var(--white);opacity:.9;flex:none}
  .brand-name{font-size:34px;line-height:1;letter-spacing:1px}
  .brand-name span{display:block;font-size:20px;margin-top:6px;letter-spacing:1.5px}
  .brand-back{left:120px;top:870px}
  .brand-front{left:640px;top:52px}

  .building{left:560px;top:190px;width:539px;height:640px;
    background:linear-gradient(180deg,rgba(255,255,255,0) 0%,#d9cfd8 25%,#8f8790 60%,#b9a6b6 85%,rgba(236,47,140,.4) 100%)}

  .title{left:583px;top:905px;width:245px;color:var(--white);font-family:var(--serif);font-weight:700;font-size:31px;line-height:1.12}
  .title small{display:block;font-weight:400;font-size:21px;margin-top:6px;letter-spacing:1px}
  .title-rule{left:842px;top:895px;width:3px;height:200px;background:var(--white)}
  .tagline{left:864px;top:900px;width:232px;color:var(--white);font-weight:700;font-size:21px;line-height:1.3;text-transform:uppercase}

  /* inside spread */
  .inside{top:1224px;height:1104px;background:var(--white);overflow:hidden}
  .fold-shadow{left:520px;top:0;width:50px;height:100%;background:linear-gradient(90deg,rgba(0,0,0,0),rgba(0,0,0,.06),rgba(0,0,0,0))}

  .garden-image{left:19px;top:48px;width:509px;height:389px;
    background:linear-gradient(180deg,#a7b0b8 0%,#7f6e5c 45%,#5b4c40 75%,#2c2a28 100%)}
  .section-title{font-family:var(--serif);font-weight:700;color:var(--ink);text-transform:uppercase;font-size:36px;line-height:1;white-space:nowrap}
  .garden-title{left:19px;top:468px;letter-spacing:1px;word-spacing:8px}
  .copy{font-size:14px;line-height:1.5;color:var(--body-ink)}
  .garden-copy{left:19px;top:518px;width:509px;text-align:justify;line-height:1.3}

  .sketch{background:linear-gradient(180deg,#fafafa,var(--sketch));border:2px solid var(--sketch-line)}
  .view-east{left:19px;top:787px;width:240px;height:281px}
  .view-south{left:274px;top:787px;width:254px;height:281px}
  .view-label{position:absolute;left:0;right:0;bottom:18px;text-align:center;font-family:var(--serif);font-weight:700;font-size:20px;color:var(--ink)}

  .reception-title{left:566px;top:26px}
  .reception-sketch{left:852px;top:17px;width:240px;height:262px}
  .subhead{font-size:22px;font-weight:400;text-transform:uppercase;color:var(--ink)}
  .challenge-head{left:564px;top:128px}
  .challenge-copy{left:564px;top:160px;width:250px;text-align:justify}
  .resolution-head{left:852px;top:292px}
  .resolution-copy{left:852px;top:324px;width:240px;text-align:justify}

  .shop-photo{left:564px;top:704px;width:530px;height:390px;
    background:linear-gradient(180deg,#f2f2f2 0%,#d8d4d0 40%,#9c8f86 75%,#6e625c 100%)}
  .floor-plan{left:574px;top:718px;width:190px;height:160px;background:linear-gradient(135deg,#ffffff,#dcdcdc);border:2px solid #999}
  .floor-plan-label{position:absolute;left:0;right:0;bottom:-30px;text-align:center;font-family:var(--serif);font-weight:700;font-size:14px;color:var(--ink);background:var(--white)}
</style>
</head>
<body>

<section class="spread cover">
  <div class="abs panel-fold"></div>

  <div class="abs contact">
    <p>Call Us- (555) 010 4872</p>
    <p>Email- gallery@quillfield.edu</p>
    <p>Visit- www.quillfieldgallery.org</p>
  </div>

  <div class="abs thumb thumb-1" role="img" aria-label="Artwork sample: colourful abstract painting"></div>
  <div class="abs thumb thumb-2" role="img" aria-label="Artwork sample: still life of apples"></div>
  <div class="abs thumb thumb-3" role="img" aria-label="Artwork sample: swirling orange abstract"></div>
  <div class="abs thumb thumb-4" role="img" aria-label="Artwork sample: dark patterned mosaic"></div>

  <div class="abs brand brand-back">
    <div class="brand-mark"></div>
    <div class="brand-name">QUILLFIELD<span>GALLERY GUILD</span></div>
  </div>

  <div class="abs brand brand-front">
    <div class="brand-mark"></div>
    <div class="brand-name">QUILLFIELD<span>GALLERY GUILD</span></div>
  </div>

  <div class="abs building" role="img" aria-label="Architectural rendering of the new gallery building with parked cars"></div>

  <h1 class="abs title">QUILLFIELD<br>GALLERY<small>RIDGE CAMPUS</small></h1>
  <div class="abs title-rule"></div>
  <p class="abs tagline">An evolutionary new space to experience the visual artswest</p>
</section>

<section class="spread inside">
  <div class="abs fold-shadow"></div>

  <div class="abs garden-image" role="img" aria-label="Rendering of the sculpture garden courtyard with seating and pergola"></div>
  <h2 class="abs section-title garden-title">Sculpture Garden</h2>
  <p class="abs copy garden-copy">Lorem ipsum dolor sit amet, consectetur adipiscing elit. Ut nibh leo, cursus et laoreet ac, lobortis vulputate orci. Nunc ultricies massa egestas malesuada pretium. Morbi congue sem ultricies dui lobortis dictum. Ut convallis quam diam, vel interdum dolor semper et. Morbi tincidunt fermentum sem sit amet iaculis. Sed ullamcorper egestas metus, quis luctus magna venenatis id. Aenean ultricies enim eget magna convallis, aliquet venenatis nisi varius. Sed varius eu lectus nec ullamcorper. Praesent ullamcorper, nulla sed lobortis ultrices, urna mi tincidunt turpis, non maximus eros ex ut eros. Aliquam tincidunt ut odio sed mollis. In et ante in nibh iaculis gravida. In arcu augue, hendrerit eget urna sit amet, mattis efficitur magna</p>

  <div class="abs sketch view-east" role="img" aria-label="Line sketch of the gallery east view interior">
    <span class="view-label">Gallery East View</span>
  </div>
  <div class="abs sketch view-south" role="img" aria-label="Line sketch of the gallery south view interior">
    <span class="view-label">Gallery South View</span>
  </div>

  <h2 class="abs section-title reception-title">Reception</h2>
  <div class="abs sketch reception-sketch" role="img" aria-label="Line sketch of the reception hallway"></div>

  <h3 class="abs subhead challenge-head">Challenge</h3>
  <p class="abs copy challenge-copy">Lorem ipsum dolor sit amet, consectetur adipiscing elit. Ut nibh leo, cursus et laoreet ac, lobortis vulputate orci. Nunc ultricies massa egestas malesuada pretium. Morbi congue sem ultricies dui lobortis dictum. Ut convallis quam diam, vel interdum dolor semper et. Morbi tincidunt fermentum sem sit amet iaculis. Sed ullamcorper egestas metus, quis luctus magna venenatis id. Aenean ultricies enim eget magna convallis, aliquet venenatis nisi varius. Sed varius eu lectus nec ullamcorper. Praesent ullamcorper, nulla sed lobortis ultrices, urna mi tincidunt turpis, non maximus eros ex ut eros. Aliquam tincidunt ut odio sed mollis. In et ante in nibh iaculis gravida. In arcu augue, hendrerit eget urna sit amet, mattis efficitur magna</p>

  <h3 class="abs subhead resolution-head">Resolution</h3>
  <p class="abs copy resolution-copy">Lorem ipsum dolor sit amet, consectetur adipiscing elit. Ut nibh leo, cursus et laoreet ac, lobortis vulputate orci. Nunc ultricies massa egestas malesuada pretium. Morbi congue sem ultricies dui lobortis dictum. Ut convallis quam diam, vel interdum dolor semper et. Morbi tincidunt fermentum sem sit amet iaculis. Sed ullamcorper egestas metus, quis luctus magna venenatis id. Aenean ultricies enim eget magna convallis, aliquet venenatis nisi varius. Sed varius eu lectus nec ullamcorper. Praesent ullamcorper, nulla sed lobortis ultrices, urna mi tincidunt turpis, non maximus</p>

  <div class="abs shop-photo" role="img" aria-label="Photo of the gallery shop display cases"></div>
  <div class="abs floor-plan" role="img" aria-label="Gallery floor plan drawing">
    <span class="floor-plan-label">Gallery Floor Plan</span>
  </div>
</section>

</body>
</html>
```